We need a poster designed for use on facebook, as well as to print out for advertising in local noticeboards and shop windows.
The poster will advertise the Fernhollow Turf Society 30th Anniversary Ball.
the ball will be held on the 28th April 2018 at the Fernhollow Community Hall.
Time will be 630pm till late. Ticket Price is $120 which includes 3 course dinner, drinks on arrival and entertainment during the evening.
Additional details will need to be added to the poster at a later date.
The fernhollow Turf Society is a horse racing club run by the community. The club has been incorporateds for 30 years. This Ball will be a celebration of that anniversary.

Target Market(s)

Middlemount Community

Industry/Entity Type

Club

Font styles to use
Serif
Decorative

Colors
1b1b1b
fbfbfb
6b449b
886aae
a64599
ffc214

Requirements
Must have
• Include
• where when time and cost
• ticket inclusions
• entertainement by Colin Hartwell
Nice to have
• Attached are some images for inspiration.
• It would be nice to have the race club logo included somewhere however not prominant.
Should not have
• Abstract geometriic lines
• images of people
• primary colours

```html
<!DOCTYPE html>
<html lang="en">
<head>
<meta charset="utf-8">
<title>Fernhollow Turf Society 30th Anniversary Ball</title>
<link rel="stylesheet" href="https://fonts.googleapis.com/css2?family=Cinzel:wght@400;500&family=Italiana&display=swap">
<style>
  :root {
    --navy: #161b27;
    --seal: #14172c;
    --black: #111111;
    --green: #a6d65e;
    --green-deep: #6f9a34;
    --white: #ececec;
    --gold: #c9a24a;
    --gold-bright: #f1cf5a;
  }
  * { margin: 0; padding: 0; box-sizing: border-box; }
  html, body { width: 926px; height: 1200px; overflow: hidden; background: #ffffff; }
  .poster {
    position: relative;
    width: 926px; height: 1200px;
    background: var(--black);
    font-family: "Cinzel", serif;
    color: var(--white);
    text-align: center;
    overflow: hidden;
  }
  .poster-frame {
    position: absolute; inset: 5px;
    border: 1px solid rgba(201,162,74,0.45);
    pointer-events: none;
  }
  .top-band {
    position: absolute; left: 0; top: 0;
    width: 100%; height: 322px;
    background: var(--navy);
  }
  .gold-rule {
    position: absolute; left: 0; top: 320px;
    width: 100%; height: 3px;
    background: linear-gradient(90deg, var(--gold), var(--gold-bright));
  }
  .seal {
    position: absolute; left: 198px; top: 50px;
    width: 530px; height: 530px;
    border-radius: 50%;
    background: radial-gradient(circle at 50% 45%, #1c2040, var(--seal) 70%);
    border: 3px solid var(--green);
    box-shadow: 0 0 0 1px var(--green-deep), 0 6px 18px rgba(0,0,0,0.6);
  }
  .club-name {
    position: absolute; left: 0; top: 58px; width: 100%;
    font-size: 11px; letter-spacing: 2px;
    color: #3a3f5a;
  }
  .title-number {
    position: absolute; left: 0; top: 78px; width: 100%;
    font-family: "Italiana", serif;
    font-size: 190px; line-height: 1;
    color: var(--green);
    letter-spacing: -4px;
  }
  .title-word {
    position: absolute; left: 0; top: 295px; width: 100%;
    font-size: 46px; line-height: 1;
    color: var(--white);
    letter-spacing: 1px;
  }
  .title-ball {
    position: absolute; left: 0; top: 345px; width: 100%;
    font-size: 74px; line-height: 1;
    color: var(--green);
    letter-spacing: 2px;
  }
  .flourish {
    position: absolute; left: 50%;
    width: 150px; height: 18px; margin-left: -75px;
    border-radius: 9px;
    background: linear-gradient(90deg, transparent, var(--green-deep) 25%, var(--green) 50%, var(--green-deep) 75%, transparent);
    opacity: 0.8;
  }
  .flourish-seal { top: 450px; }
  .flourish-foot { top: 1140px; }
  .details { position: absolute; left: 0; top: 615px; width: 100%; }
  .lead { font-size: 20px; color: var(--white); letter-spacing: 1px; }
  .highlight { color: var(--green); font-size: 28px; letter-spacing: 1px; }
  .date { margin-top: 8px; }
  .time { font-size: 24px; margin-top: 4px; }
  .venue-lead { margin-top: 34px; }
  .venue { margin-top: 8px; font-size: 28px; }
  .ticket {
    position: relative;
    width: 676px; height: 98px;
    margin: 52px auto 0;
    border: 1px solid var(--gold);
  }
  .ticket-price {
    position: absolute; left: 50%; top: -19px;
    transform: translateX(-50%);
    padding: 0 10px;
    background: var(--black);
    white-space: nowrap;
    font-size: 26px; color: var(--green);
  }
  .ticket-includes {
    padding-top: 30px;
    font-size: 16px; line-height: 30px;
    color: var(--white); letter-spacing: 0.5px;
  }
  .entertainer-lead { margin-top: 52px; }
  .entertainer { margin-top: 12px; }
</style>
</head>
<body>
<main class="poster">
  <div class="top-band"></div>
  <div class="gold-rule"></div>

  <section class="seal">
    <p class="club-name">Fernhollow Turf Society</p>
    <h1>
      <span class="title-number">30th</span>
      <span class="title-word">Anniversary</span>
      <span class="title-ball">Ball</span>
    </h1>
    <div class="flourish flourish-seal" role="img" aria-label="Green scroll ornament"></div>
  </section>

  <section class="details">
    <p class="lead">The ball will be held on</p>
    <p class="highlight date">Saturday &nbsp;|&nbsp; 28th April &nbsp;|&nbsp; 2018</p>
    <p class="highlight time">Time will be 6:30pm</p>
    <p class="lead venue-lead">at</p>
    <p class="highlight venue">Fernhollow Community Hall.</p>

    <div class="ticket">
      <p class="ticket-price">Ticket Price is $120</p>
      <p class="ticket-includes">which includes 3 course dinner, drinks on arrival and<br>entertainment during the</p>
    </div>

    <p class="lead entertainer-lead">Entertainement by</p>
    <p class="highlight entertainer">Colin Hartwell</p>
  </section>

  <div class="flourish flourish-foot" role="img" aria-label="Green scroll ornament"></div>
  <div class="poster-frame"></div>
</main>
</body>
</html>
```